Creation of a cover for a book with an image provided. It is mainly a typographical work. PICTURE (Quiet Harbor IV) IS NOW AVAILABLE

Target Market(s)

General Public

Colors

Designer to choose colors to be used in the design.

Requirements
Must have
• Upper edge: "Mireille Fontaz" (author) Title: "Rain before the harvest" Bottom edge: "Marrow Editions"

```html
<!DOCTYPE html>
<html lang="en">
<head>
<meta charset="utf-8">
<title>Rain before the harvest — Mireille Fontaz</title>
<link href="https://fonts.googleapis.com/css2?family=Prata&display=swap" rel="stylesheet">
<style>
  :root {
    --page-bg: #ffffff;
    --ink-light: #ffffff;
    --violet: #6a4aa8;
    --violet-deep: #4a3c8e;
    --sky: #5ec8ee;
    --cobalt: #3f5fb8;
    --rose: #f0468e;
    --magenta: #e0206a;
    --blush: #f6c6dc;
    --ember: #e8582a;
  }
  * { margin: 0; padding: 0; box-sizing: border-box; }
  html, body {
    width: 1000px;
    height: 1200px;
    overflow: hidden;
    background: var(--page-bg);
  }
  .canvas {
    position: relative;
    width: 1000px;
    height: 1200px;
  }
  .book-cover {
    position: absolute;
    left: 200px;
    top: 100px;
    width: 600px;
    height: 1000px;
    overflow: hidden;
    font-family: "Prata", "Times New Roman", serif;
    color: var(--ink-light);
    text-align: center;
  }
  .cover-artwork {
    position: absolute;
    inset: 0;
    background:
      radial-gradient(ellipse 45% 22% at 20% 8%, var(--violet) 0%, transparent 100%),
      radial-gradient(ellipse 40% 20% at 85% 10%, var(--sky) 0%, transparent 100%),
      radial-gradient(ellipse 35% 30% at 10% 40%, var(--rose) 0%, transparent 100%),
      radial-gradient(ellipse 40% 35% at 85% 50%, var(--cobalt) 0%, transparent 100%),
      radial-gradient(ellipse 30% 18% at 20% 72%, var(--blush) 0%, transparent 100%),
      radial-gradient(ellipse 35% 25% at 55% 68%, var(--magenta) 0%, transparent 100%),
      radial-gradient(ellipse 30% 15% at 85% 75%, var(--sky) 0%, transparent 100%),
      radial-gradient(ellipse 30% 18% at 8% 88%, var(--ember) 0%, transparent 100%),
      radial-gradient(ellipse 60% 20% at 50% 96%, var(--magenta) 0%, transparent 100%),
      linear-gradient(160deg, var(--violet-deep) 0%, var(--rose) 45%, var(--cobalt) 75%, var(--magenta) 100%);
  }
  .cover-author {
    position: absolute;
    top: 62px;
    left: 0;
    right: 0;
    font-size: 27px;
    letter-spacing: 1px;
    text-transform: uppercase;
  }
  .cover-title {
    position: absolute;
    top: 270px;
    left: 0;
    right: 0;
    font-size: 74px;
    font-weight: 400;
    line-height: 1.08;
    text-transform: uppercase;
  }
  .cover-title span { display: block; }
  .cover-publisher {
    position: absolute;
    bottom: 95px;
    left: 0;
    right: 0;
    font-size: 24px;
    letter-spacing: 1px;
    text-transform: uppercase;
  }
</style>
</head>
<body>
  <main class="canvas">
    <section class="book-cover">
      <div class="cover-artwork" role="img" aria-label="Abstract textured paint strokes in violet, sky blue, cobalt, pink and magenta"></div>
      <p class="cover-author">Mireille Fontaz</p>
      <h1 class="cover-title">
        <span>Rain</span>
        <span>before</span>
        <span>the</span>
        <span>harvest</span>
      </h1>
      <p class="cover-publisher">Marrow Editions</p>
    </section>
  </main>
</body>
</html>
```